we are an outdoor outlet in a country club that has a variety of outlets. The Club is called Brookhaven and is located in Cairo, Egypt. This garden menu will include cuisines from the Mediterranean, Asia and Texmex. we need a menu that is colorful and would fit an A3 size, back and front are to be used. Attached is the old menu currently in use (Garden Menu 2012.pdf is just for reference) and the new menu text for you to use is under the name Garden Menu Fall 2013
thank you.

```html
<!DOCTYPE html>
<html lang="en">
<head>
<meta charset="utf-8">
<title>Brookhaven Garden Menu Fall 2013</title>
<link rel="stylesheet" href="https://fonts.googleapis.com/css2?family=Berkshire+Swash&family=Questrial&family=Arimo:wght@400;700&display=swap">
<style>
  :root {
    --paper: #fcf7d6;
    --band: #dd6a2c;
    --band-dark: #c9551f;
    --brown: #5a3413;
    --footer: #5b3a12;
    --orange: #de6a25;
    --green: #8cae3a;
    --footer-green: #c9e27a;
    --ink: #1b1b1b;
    --white: #ffffff;
    --photo-salad: #9a8a5a;
    --photo-dessert: #e8b24a;
    --photo-garden: #f3efd9;
  }
  * { box-sizing: border-box; margin: 0; padding: 0; }
  html, body { width: 848px; height: 1200px; overflow: hidden; }
  body { background: var(--paper); font-family: "Arimo", Arial, sans-serif; color: var(--ink); }
  .menu { position: relative; width: 848px; height: 1200px; overflow: hidden; background: var(--paper); }

  .header-band {
    position: absolute; left: 0; top: 0; width: 848px; height: 106px;
    background: linear-gradient(180deg, var(--band-dark), var(--band));
  }
  .menu-title {
    position: absolute; left: 22px; top: 18px;
    font-family: "Berkshire Swash", cursive; font-weight: 400;
    font-size: 51px; color: var(--white); letter-spacing: 0.5px;
  }
  .brand-box {
    position: absolute; left: 536px; top: -10px; width: 298px; height: 106px;
    background: var(--white); border-radius: 0 0 14px 14px;
    display: flex; align-items: center; justify-content: center; gap: 14px; padding-top: 10px;
  }
  .brand-dot { width: 40px; height: 40px; border-radius: 50%; background: var(--green); }
  .brand-name { font-family: "Questrial", sans-serif; font-size: 38px; color: var(--green); }

  .column { position: absolute; }
  .col-left { left: 16px; top: 126px; width: 400px; }
  .col-right { left: 432px; top: 120px; width: 404px; }

  .cuisine {
    font-family: "Berkshire Swash", cursive; font-weight: 400;
    font-size: 27px; color: var(--brown); line-height: 34px;
    border-bottom: 1px solid var(--brown); padding-bottom: 1px;
  }
  .course {
    font-family: "Questrial", sans-serif; font-size: 23px; color: var(--orange);
    line-height: 28px; margin: 12px 0 8px;
  }
  .item { font-size: 13.5px; line-height: 17px; margin-bottom: 6px; width: 360px; }
  .price { color: var(--green); }

  .photo { border: 2px solid var(--orange); border-radius: 12px; }
  .photo-salad {
    width: 334px; height: 120px; margin: 16px 0 6px;
    background: radial-gradient(ellipse at 45% 50%, #8b6a44, var(--photo-salad) 55%, #dfe0d0);
  }
  .photo-dessert {
    position: absolute; left: 500px; top: 560px; width: 336px; height: 120px;
    background: linear-gradient(90deg, #f1f1ee 0%, #d84a3a 30%, #f4f2ee 50%, var(--photo-dessert) 72%, #f1f0ec 100%);
  }
  .col-right .item { width: 366px; }
  .desserts { position: absolute; left: 432px; top: 684px; width: 404px; }
  .desserts .cuisine { margin-bottom: 8px; }
  .desserts .item { margin-bottom: 5.5px; width: 380px; }

  .footer {
    position: absolute; left: 16px; top: 1087px; width: 652px; height: 96px;
    background: var(--footer); border-radius: 8px;
    font-family: "Questrial", sans-serif; color: var(--footer-green);
  }
  .contact { position: absolute; left: 13px; top: 8px; font-size: 22px; line-height: 27px; }
  .contact strong { font-family: "Arimo", sans-serif; font-weight: 700; color: var(--white); font-size: 24px; }
  .hours { position: absolute; left: 389px; top: 10px; font-size: 19px; line-height: 24px; }
  .hours strong { font-family: "Arimo", sans-serif; font-weight: 700; color: var(--white); font-size: 18px; }
  .garden-illustration {
    position: absolute; left: 680px; top: 1050px; width: 160px; height: 140px;
    background: radial-gradient(ellipse at 55% 40%, #e69a8f 0%, #f2d3c6 30%, var(--photo-garden) 60%, rgba(243,239,217,0) 78%);
  }
</style>
</head>
<body>
<main class="menu">
  <header>
    <div class="header-band"></div>
    <h1 class="menu-title">Garden Menu Fall 2013</h1>
    <div class="brand-box"><span class="brand-dot"></span><span class="brand-name">Brookhaven</span></div>
  </header>

  <section class="column col-left">
    <h2 class="cuisine">Asian Corner</h2>
    <h3 class="course">Salads &amp; Appetizers</h3>
    <p class="item">Chicken Wasabi Salad......<span class="price">00.00 L.E.</span></p>
    <p class="item" style="width:345px">Diced chicken with a mayo wasabi dressing on top of shredded lettuce......<span class="price">00.00 L.E.</span></p>
    <p class="item">Chicken Sesame Noodle Salad......<span class="price">00.00 L.E.</span></p>
    <p class="item" style="width:350px">Sesame crusted chicken with glass noodles tossed with sweet chili, soy sauce, and lemongrass......<span class="price">00.00 L.E.</span></p>
    <p class="item">Spring rolls......<span class="price">00.00 L.E.</span></p>
    <p class="item" style="width:350px">Vegetable spring rolls served with house made sweet and sour dip......<span class="price">00.00 L.E.</span></p>
    <p class="item">Indian Samosa......<span class="price">00.00 L.E.</span></p>
    <p class="item" style="width:280px">Fried dough parcels filled with vegetables and spices......<span class="price">00.00 L.E.</span></p>
    <div class="photo photo-salad" role="img" aria-label="Photo of grilled chicken slices on a vegetable salad"></div>
    <h3 class="course">Main Courses</h3>
    <p class="item">Murgh Chicken Makhni......&nbsp;&nbsp;&nbsp;&nbsp;&nbsp;<span class="price">00.00 L.E.</span></p>
    <p class="item">Chicken cubes in a rich creamy tomato sauce seasoned with garam masala......&nbsp;&nbsp;&nbsp;<span class="price">00.00 L.E.</span></p>
    <p class="item" style="width:400px">Choice of side: vegetable korma or curd......&nbsp;&nbsp;&nbsp;&nbsp;&nbsp;&nbsp;&nbsp;&nbsp;<span class="price">00.00 L.E.</span></p>
    <p class="item">Chicken Tandoori......&nbsp;&nbsp;&nbsp;&nbsp;<span class="price">00.00 L.E.</span></p>
    <p class="item" style="width:355px">Grilled chicken cubes with tandoori spices served with basmati rice.....&nbsp;&nbsp;&nbsp;<span class="price">00.00 L.E.</span></p>
    <p class="item">Thai Coconut Curry Shrimp...&nbsp;&nbsp;&nbsp;&nbsp;&nbsp;<span class="price">00.00 L.E.</span></p>
    <p class="item" style="width:340px">Sautéed shrimp tossed with curry and coconut milk served with jasmine rice......&nbsp;&nbsp;&nbsp;<span class="price">00.00 L.E.</span></p>
    <p class="item">Mongolian Beef....&nbsp;&nbsp;&nbsp;<span class="price">00.00 L.E.</span></p>
    <p class="item" style="width:355px">Soy marinated beef with oyster sauce and vegetables served with egg noodles......&nbsp;&nbsp;&nbsp;&nbsp;&nbsp;<span class="price">00.00 L.E.</span></p>
    <h2 class="cuisine" style="margin-top:30px">Tex Mex</h2>
    <h3 class="course">Salads &amp; Appetizers</h3>
    <p class="item">Caesar Salad......<span class="price">00.00 L.E.</span></p>
    <p class="item" style="width:320px">Iceberg lettuce with Caesar dressing with grated Parmesan cheese and croutons......<span class="price">00.00 L.E.</span></p>
  </section>

  <section class="column col-right">
    <p class="item">Taco salad42......<span class="price">00.00 L.E.</span></p>
    <p class="item" style="width:362px">Chicken breast, beans, sour cream, guacamole, tomato, corn, lettuce, olives, chives, vinaigrette......<span class="price">00.00 L.E.</span></p>
    <p class="item" style="width:280px">Nachos topped with chili, melted cheese, beans...<span class="price">00.00 L.E.</span></p>
    <p class="item" style="width:355px">Chicken Quesadilla served with guacamole, salsa, and sour cream......<span class="price">00.00 L.E.</span></p>
    <h3 class="course">Main Courses &amp; Sandwiches</h3>
    <p class="item">Cheeseburger....<span class="price">00.00 L.E.</span></p>
    <p class="item" style="width:340px">House made lean beef burger topped with cheddar cheese....<span class="price">00.00 L.E.</span></p>
    <p class="item">Mushroom Burger....<span class="price">00.00 L.E.</span></p>
    <p class="item" style="width:370px">Beef burger with sautéed mushroom, caramelized onion, and provolone cheese......<span class="price">00.00 L.E.</span></p>
    <p class="item">Crispy Chicken Wrap ......<span class="price">00.00 L.E.</span></p>
    <p class="item" style="width:260px">Crisp fried chicken wrap with a ranch dressing......<span class="price">00.00 L.E.</span></p>
    <p class="item">Fajita (Chicken, Beef, Combo)......<span class="price">00.00 L.E.</span></p>
    <p class="item" style="width:375px">Pan seared meat or chicken with onion and bell pepper served with sour cream, guacamole, salsa......<span class="price">00.00 L.E.</span></p>
  </section>

  <div class="photo photo-dessert" role="img" aria-label="Photo of fresh strawberries beside a pumpkin flan with passion fruit"></div>

  <section class="desserts">
    <h2 class="cuisine">Desserts</h2>
    <p class="item">Mix Berries Cheesecake......<span class="price">00.00 L.E.</span></p>
    <p class="item">Crème Brulee......<span class="price">00.00 L.E.</span></p>
    <p class="item">Chocolate Caramel Cake......<span class="price">00.00 L.E.</span></p>
    <p class="item">Warm Chocolate Fondant......<span class="price">00.00 L.E.</span></p>
    <p class="item">Baked Apple Tart Tatin......<span class="price">00.00 L.E.</span></p>
    <p class="item">Tiramisu......<span class="price">00.00 L.E.</span></p>
    <p class="item">Pumpkin Pie Flan......<span class="price">00.00 L.E.</span></p>
    <p class="item">Mixed Berries Granola Yoghurt.....<span class="price">00.00 L.E.</span></p>
    <p class="item" style="width:330px">Vanilla Ice Cream Profiterole with dark and white chocolate sauce.....<span class="price">00.00 L.E.</span></p>
    <p class="item" style="width:245px">Caramelized Banana with Deep Fried Ice Cream......<span class="price">00.00 L.E.</span></p>
    <p class="item">Baklava with Nuts and Sugar Syrup.....<span class="price">00.00 L.E.</span></p>
    <p class="item" style="width:378px">Shot Glass Sampler – Tiramisu, Chocolate Crisp Mousse, Pear with Sabayon.....<span class="price">00.00 L.E.</span></p>
    <p class="item">Ice Cream by Scoop......<span class="price">00.00 L.E.</span></p>
  </section>

  <div class="garden-illustration" role="img" aria-label="Sketch of a garden table and chairs under a red umbrella"></div>

  <footer class="footer">
    <div class="contact">
      Phone : <strong>000 000 0000</strong><br>
      www.brookhaven-gardenmenu.com<br>
      Address:
    </div>
    <div class="hours">
      Mon-Fri <strong>11.00 am to 9.00 pm</strong><br>
      Sat-Sun <strong>4.00 pm to 9.00 pm</strong>
    </div>
  </footer>
</main>
</body>
</html>
```